Non Profit Company Looking For New Website

The website for Corvale Paddock Rehoming Society should offer the viewer beautiful photos that inspire condifence and joy and tap into our love of horses.

We would like to see a website that displays trust, quality and confidence. Needs to be responsive and mobile friendly for all browsers and coded for both Android & IOS.

READ ATTACHED WEBSITE TEMPLATE FOR COMPLETE DETAILS ON WHAT WE ARE LOOKING FOR.

Looking for recommmendations if we should use WordPress/WooCommerce for site or Wordpress with Shopify Plug in or just Shopify.

Must be both desktop and mobile friendly with fast page load speed. Need the ability to edit ourselves.

Industry/Entity Type

Non Profit

Coding

Coded - Design and coding required

Number of Pages Required

5+ page

Requirements
Must have
• We would like to see a website that displays trust, quality and confidence. Needs to be responsive and mobile friendly for all browsers and coded for both Android & IOS.

Looking for recommendations if we should use WordPress/WooCommerce for site or Wordpress with Shopify Plug in or just Shopify.

Logo Colour:
Pantone 7621 C

READ TEMPLATE THAT IS ATTACHED
Nice to have
• Like look of this website as a sample:
https://www.quillmanegallop.com/

Another similar non profit organization
https://brindlefieldrest.com/

```html
<!DOCTYPE html>
<html lang="en">
<head>
<meta charset="utf-8">
<title>Corvale Paddock Rehoming Society — Home</title>
<link href="https://fonts.googleapis.com/css2?family=Playfair+Display:wght@400;600;700&family=Lora:wght@400;600;700&display=swap" rel="stylesheet">
<style>
:root{
  --board:#ad2027;
  --brand:#ab2328;
  --green:#17b84a;
  --ink:#1e1b18;
  --muted:#5b5650;
  --soft:#efefef;
  --white:#fff;
  --teal:#1bb39a;
  --link:#4a6fd1;
}
*{box-sizing:border-box;margin:0;padding:0}
html,body{width:1200px;height:2349px;overflow:hidden}
body{background:var(--board);font-family:'Lora',Georgia,serif;color:var(--ink);position:relative}
.serif{font-family:'Playfair Display',Georgia,serif}
.screen{position:absolute;top:70px;background:var(--white);overflow:hidden}
.desktop{left:188px;width:652px;height:2176px}
.mobile{left:907px;width:105px;height:2176px}
section,header,footer{position:relative;width:100%}
.btn{display:inline-flex;align-items:center;justify-content:center;border-radius:999px;font-weight:700;text-transform:uppercase;letter-spacing:.02em;white-space:nowrap}
.btn-green{background:var(--green);color:var(--white)}
.btn-ghost{border:1px solid var(--green);color:var(--green)}
.btn-submit{border:1.5px solid var(--brand);color:var(--brand);background:var(--white);font-weight:400;text-transform:none}
.photo{display:block}
.center{text-align:center}
.brandname{font-family:'Playfair Display',Georgia,serif;font-weight:600;color:var(--brand);line-height:1.1}

/* ---------- desktop ---------- */
.d-header{height:44px;display:flex;align-items:center;justify-content:space-between;padding:0 28px 0 27px}
.d-header .brandname{font-size:7px;width:54px;text-align:center}
.d-nav{display:flex;align-items:center;gap:13px;font-size:5px;text-transform:uppercase;letter-spacing:.04em}
.d-nav .active{color:var(--brand)}
.d-nav .pill{border:1px solid var(--ink);border-radius:999px;padding:4px 5px}
.d-hero{height:251px;background:linear-gradient(180deg,#2f4a22 0%,#3d6a2a 45%,#2e6a1f 70%,#1f4d16 100%);display:flex;flex-direction:column;align-items:center;padding-top:62px}
.d-hero h1{color:var(--white);font-size:22px;line-height:1.08;font-weight:700;text-align:center;width:400px}
.d-hero .ctas{display:flex;gap:4px;margin-top:30px}
.d-hero .btn{height:18px;font-size:5px;padding:0 11px}
.d-retire{height:324px;background:var(--soft);padding-top:34px}
.d-retire h2{font-size:22px;line-height:1.2;font-weight:600}
.d-retire p{font-size:6.5px;line-height:1.7;width:216px;margin:12px auto 0}
.d-retire .photo{position:absolute;left:200px;bottom:0;width:250px;height:190px;background:radial-gradient(ellipse at 50% 70%,#cfcfcf 0%,#e6e6e6 45%,var(--soft) 75%)}
.d-about{height:258px;padding-top:32px}
.d-about h2{font-size:16px;line-height:1.2;font-weight:600}
.d-about p{font-size:6.5px;line-height:1.7;width:218px;margin:0 auto}
.d-about p.first{margin-top:26px}
.d-about p+p{margin-top:10px}
.d-about .btn{margin-top:25px;height:19px;font-size:5.5px;padding:0 11px}
.d-adopt{height:359px;display:flex}
.d-adopt .copy{width:326px;display:flex;flex-direction:column;align-items:center;justify-content:center;padding-top:10px}
.d-adopt h2{font-size:16px;font-weight:600}
.d-adopt p{font-size:5.5px;line-height:1.7;width:210px;margin-top:8px;color:var(--muted)}
.d-adopt .btn{margin-top:9px;height:19px;font-size:5.5px;padding:0 11px}
.d-adopt .photo{width:326px;height:359px;background:radial-gradient(circle at 30% 20%,#f6e27a 0%,#d9a81f 35%,#8a5a12 70%,#4a2e0d 100%)}
.d-horses{height:400px;padding-top:28px}
.d-horses h2{font-size:20px;font-weight:600}
.d-cards{display:flex;justify-content:center;gap:11px;margin-top:28px}
.card{width:62px;text-align:center;font-size:5.5px;line-height:1.45}
.card .photo{width:62px;height:68px;background:linear-gradient(180deg,#9cc3e6 0%,#b9cfd9 35%,#6b8a3f 60%,#4f6a2c 100%)}
.card .name{font-family:'Playfair Display',Georgia,serif;font-size:6.5px;margin-top:8px;color:var(--muted)}
.card .tag{display:inline-block;background:var(--teal);color:var(--white);font-size:2.5px;padding:1px 4px;margin-top:3px;text-transform:uppercase}
.card .fee{font-weight:700;font-size:6.5px;line-height:1.35;margin-top:8px}
.card .row{font-weight:600;font-size:5px}
.card .gap{margin-top:10px}
.card .read{color:var(--link);font-size:4.5px;border-bottom:1px solid var(--link);display:inline-block;margin-top:18px}
.d-horses .btn{display:flex;width:87px;margin:24px auto 0;height:19px;font-size:5.5px}
.d-contact{height:392px;background:var(--soft);padding-top:36px}
.d-contact h2{font-size:16px;font-weight:600;line-height:1.2}
.d-contact .lede{font-size:5.5px;margin-top:12px;color:var(--muted)}
.d-contact .grid{position:absolute;top:115px;left:122px;right:122px;display:flex}
.info{font-size:5.5px;line-height:1.75;color:var(--muted)}
.info h3{font-family:'Playfair Display',Georgia,serif;font-size:8px;color:var(--ink);font-weight:600;margin-top:9px;line-height:1.2}
.pin{width:10px;height:10px;display:block}
.d-form{position:absolute;top:108px;left:350px;width:188px}
.field label{display:block;font-size:5.5px;font-weight:700}
.field label b{color:var(--brand)}
.field .input{background:var(--white);border:1px solid #d8d8d8;border-radius:3px;height:16px;margin-top:4px}
.d-form .field{margin-bottom:18px}
.d-form .field:last-of-type .input{height:67px}
.d-form .btn{display:flex;width:97px;height:16px;margin:-5px auto 0;font-size:6px}
.d-gap{height:12px}
.d-footer{height:136px;background:var(--soft);padding:22px 122px 0}
.d-footer .cols{display:flex;gap:22px}
.foot-addr{font-size:5px;line-height:1.6;color:var(--muted);width:84px}
.foot-addr strong{font-family:'Playfair Display',Georgia,serif;color:var(--ink);display:block;margin-bottom:10px;line-height:1.3}
.foot-links{font-size:5px;line-height:2.25;color:var(--muted)}
.foot-links .pill{border:1px solid var(--muted);border-radius:999px;padding:1px 4px}
.d-footer .bottom{position:absolute;left:122px;right:122px;bottom:15px;display:flex;justify-content:space-between;align-items:center;font-size:4.5px;color:var(--muted)}
.social{display:flex;gap:8px}
.social span{width:6px;height:6px;border:1px solid var(--ink);display:block}
.social span.round{border-radius:50%}

/* ---------- mobile ---------- */
.m-header{height:39px;display:flex;justify-content:space-between;align-items:flex-start;padding:6px 6px 0 6px}
.m-header .brandname{font-size:4px;width:28px;text-align:center}
.m-menu{font-size:3.5px;color:var(--muted);margin-top:11px;letter-spacing:.05em}
.m-hero{height:180px;background:linear-gradient(180deg,#2f4a22 0%,#3d6a2a 50%,#1f4d16 100%);padding-top:26px;display:flex;flex-direction:column;align-items:center}
.m-hero h1{color:var(--white);font-size:10.5px;line-height:1.15;text-align:center;width:92px;font-weight:700}
.m-hero .btn-ghost{margin-top:19px;width:88px;height:12px;font-size:3.5px}
.m-hero .btn-green{margin-top:7px;width:47px;height:14px;font-size:4px}
.m-retire{height:147px;background:var(--soft);padding-top:26px}
.m-retire h2{font-size:10.5px;font-weight:600;line-height:1.25}
.m-retire p{font-size:4.5px;line-height:1.7;width:90px;margin:7px auto 0}
.m-retire .photo{position:absolute;left:24px;bottom:0;width:58px;height:48px;background:radial-gradient(ellipse at 50% 70%,#cdcdcd 0%,#e4e4e4 45%,var(--soft) 75%)}
.m-about{height:254px;padding-top:25px}
.m-about h2{font-size:9px;font-weight:600;line-height:1.3}
.m-about p{font-size:4.5px;line-height:1.75;width:96px;margin:0 auto;color:var(--muted)}
.m-about p.first{margin-top:13px}
.m-about p+p{margin-top:7px}
.m-about .btn{margin-top:17px;height:14px;width:78px;font-size:4px}
.m-adopt-photo{height:117px;background:radial-gradient(circle at 30% 25%,#f6e27a 0%,#d9a81f 40%,#7d5212 80%)}
.m-adopt{height:97px;padding-top:18px}
.m-adopt h2{font-size:9px;font-weight:600}
.m-adopt p{font-size:3.8px;line-height:1.7;width:96px;margin:5px auto 0;color:var(--muted)}
.m-adopt .btn{margin-top:7px;width:48px;height:14px;font-size:4px}
.m-horses{height:669px;padding-top:21px}
.m-horses h2{font-size:10.5px;font-weight:600}
.m-horses .cards{display:flex;flex-direction:column;align-items:center;gap:10px;margin-top:14px}
.m-horses .card{width:85px;font-size:4px}
.m-horses .card .photo{width:85px;height:56px}
.m-horses .card .name{font-size:5px;margin-top:5px}
.m-horses .card .fee{font-size:5px;margin-top:5px}
.m-horses .card .row{font-size:3.8px}
.m-horses .card .gap{margin-top:6px}
.m-horses .card .read{font-size:3.5px;margin-top:9px}
.m-horses .btn{display:flex;width:71px;height:15px;margin:11px auto 0;font-size:4px}
.m-contact{height:479px;background:var(--soft);padding:24px 7px 0}
.m-contact h2{font-size:9.5px;font-weight:600;line-height:1.25}
.m-contact .lede{font-size:3.8px;color:var(--muted);margin-top:5px}
.m-contact .info{font-size:4px;line-height:1.7;margin-top:20px}
.m-contact .info h3{font-size:5.5px;margin-top:5px}
.m-contact .info+.info{margin-top:9px}
.m-contact .pin{width:8px;height:8px}
.m-form{margin-top:3px;padding:0 1px}
.m-form .field{margin-bottom:9px}
.m-form .field label{font-size:3.8px}
.m-form .field .input{height:13px;margin-top:2px}
.m-form .field:last-of-type .input{height:56px}
.m-form .btn{display:flex;width:55px;height:13px;margin:9px auto 0;font-size:4px}
.m-gap{height:8px}
.m-footer{height:186px;background:var(--soft);padding:22px 6px 0}
.m-footer .foot-addr{font-size:3.5px;width:auto}
.m-footer .foot-addr strong{margin-bottom:7px}
.m-footer .foot-links{font-size:3.5px;line-height:2.45;margin-top:10px}
.m-footer .social{margin-top:19px;gap:7px}
.m-footer .social span{width:5px;height:5px}
.m-footer .copy{font-size:3.5px;line-height:1.6;color:var(--muted);margin-top:5px}
</style>
</head>
<body>

<svg width="0" height="0" style="position:absolute" aria-hidden="true">
  <defs>
    <symbol id="icon-pin" viewBox="0 0 20 20">
      <circle cx="10" cy="10" r="10" fill="#ab2328"/>
      <path d="M10 4.5a3.6 3.6 0 0 0-3.6 3.6c0 2.7 3.6 6.9 3.6 6.9s3.6-4.2 3.6-6.9A3.6 3.6 0 0 0 10 4.5z" fill="#fff"/>
      <circle cx="10" cy="8.1" r="1.3" fill="#ab2328"/>
    </symbol>
  </defs>
</svg>

<!-- Desktop screen -->
<main class="screen desktop">
  <header class="d-header">
    <div class="brandname">Corvale Paddock Rehoming Society</div>
    <nav class="d-nav">
      <span class="active">Home</span><span>About</span><span>Adopt</span><span>Horses</span>
      <span class="pill">Donate &amp; Shop</span><span>Contact Us</span>
    </nav>
  </header>

  <section class="d-hero" role="img" aria-label="Photo of a bay horse grazing in a green paddock beside white fences and willow trees">
    <h1 class="serif">We support and develop retired thoroughbred racehorses for their next chapter in life</h1>
    <div class="ctas">
      <span class="btn btn-ghost">Adopt a Thoroughbred</span>
      <span class="btn btn-green">Donate Us</span>
    </div>
  </section>

  <section class="d-retire center">
    <h2 class="serif">Retire. Retrain.<br>Rehome.</h2>
    <p><strong>Corvale Paddock Rehoming Society</strong> (CPRS) is a registered not-for-profit organization in Alberta.</p>
    <div class="photo" role="img" aria-label="Soft black and white photo of a grey horse's head and mane"></div>
  </section>

  <section class="d-about center">
    <h2 class="serif">What is Thoroughbred<br>Aftercare?</h2>
    <p class="first">The <strong>health</strong>, <strong>safety</strong> and <strong>welfare</strong> of our equine athletes does not end at the finish line, and retirement and aftercare are critical to the success of the racing industry.</p>
    <p>Aftercare is the safe placement of racehorses after their careers as racehorse are completed. Some horses might retire to the breeding shed or broodmare bands, while others are retrained for second careers.</p>
    <span class="btn btn-green">Learn More About Us</span>
  </section>

  <section class="d-adopt">
    <div class="copy center">
      <h2 class="serif">Adopt a Horse</h2>
      <p>Corvale Paddock Rehoming is committed to helping match you with the perfect horse.</p>
      <span class="btn btn-green">Adopt Now</span>
    </div>
    <div class="photo" role="img" aria-label="Sunlit photo of a woman greeting a dark bay horse in a meadow of golden light"></div>
  </section>

  <section class="d-horses center">
    <h2 class="serif">Our Horses</h2>
    <div class="d-cards">
      <article class="card">
        <div class="photo" role="img" aria-label="Photo of Marlowe Bay, a bay gelding standing in a field"></div>
        <div class="name">Marlowe Bay</div>
        <span class="tag">Our Horses</span>
        <div class="fee">FEE $1,000—NOW $800 UNTIL 5/31</div>
        <div class="row">Height 15.3</div>
        <div class="row gap">Birth Year 2016</div>
        <div class="row" style="margin-top:4px">Color Bay<br>Gender Gelding</div>
        <div class="row gap">Location</div>
        <div class="row" style="margin-top:18px">LEXINGTON, KY</div>
        <span class="read">Read More</span>
      </article>
      <article class="card">
        <div class="photo" role="img" aria-label="Photo of Tobin Reel, a chestnut gelding by a fence"></div>
        <div class="name">Tobin Reel</div>
        <span class="tag">Our Horses</span>
        <div class="fee">FEE $1,000—NOW $800 UNTIL 5/31</div>
        <div class="row">Height 15.3</div>
        <div class="row gap">Birth Year 2016</div>
        <div class="row" style="margin-top:4px">Color Bay<br>Gender Gelding</div>
        <div class="row gap">Location</div>
        <div class="row" style="margin-top:18px">LEXINGTON, KY</div>
        <span class="read">Read More</span>
      </article>
      <article class="card">
        <div class="photo" role="img" aria-label="Photo of Quiet Harbor, a dark bay gelding in a paddock"></div>
        <div class="name">Quiet Harbor</div>
        <span class="tag">Our Horses</span>
        <div class="fee">FEE $1,000—NOW $800 UNTIL 5/31</div>
        <div class="row">Height 15.3</div>
        <div class="row gap">Birth Year 2016</div>
        <div class="row" style="margin-top:4px">Color Bay<br>Gender Gelding</div>
        <div class="row gap">Location</div>
        <div class="row" style="margin-top:18px">LEXINGTON, KY</div>
        <span class="read">Read More</span>
      </article>
    </div>
    <span class="btn btn-green">More Ways to Give</span>
  </section>

  <section class="d-contact center">
    <h2 class="serif">Have a question or need<br>more information?</h2>
    <p class="lede">Give us a call or use the form below.</p>
    <div class="grid" style="text-align:left">
      <div class="info" style="width:108px">
        <svg class="pin"><use href="#icon-pin"/></svg>
        <h3>Location</h3>
        42 Larkspur Run<br>Fenwick Hollow<br>British Columbia<br>V0X 2B7
      </div>
      <div>
        <div class="info">
          <svg class="pin"><use href="#icon-pin"/></svg>
          <h3>Call Us</h3>
          +1 555 014 2290
        </div>
        <div class="info" style="margin-top:14px">
          <svg class="pin"><use href="#icon-pin"/></svg>
          <h3>E-Mail</h3>
          info@corvalepaddock.org
        </div>
      </div>
    </div>
    <form class="d-form" style="text-align:left">
      <div class="field"><label>Name <b>*</b></label><div class="input"></div></div>
      <div class="field"><label>Email <b>*</b></label><div class="input"></div></div>
      <div class="field"><label>Phone</label><div class="input"></div></div>
      <div class="field"><label>Message <b>*</b></label><div class="input"></div></div>
      <span class="btn btn-submit">Submit</span>
    </form>
  </section>

  <div class="d-gap"></div>

  <footer class="d-footer">
    <div class="cols">
      <div class="foot-addr">
        <strong>Corvale Paddock Rehoming Society</strong>
        42 Larkspur Run<br>Fenwick Hollow<br>British Columbia<br>V0X 2B7<br>555-018-7734
      </div>
      <div class="foot-links">
        Home<br>About<br>Adopt<br>Horses<br><span class="pill">Donate &amp; Shop</span><br>Contact Us
      </div>
    </div>
    <div class="bottom">
      <span>Copyright © 2021. 0.0.0b. - Dev version</span>
      <div class="social"><span class="round"></span><span class="round"></span><span></span></div>
    </div>
  </footer>
</main>

<!-- Mobile screen -->
<main class="screen mobile">
  <header class="m-header">
    <div class="brandname">Corvale Paddock Rehoming Society</div>
    <span class="m-menu">MENU ☰</span>
  </header>

  <section class="m-hero" role="img" aria-label="Photo of a horse grazing in a green paddock with white fences">
    <h1 class="serif">We support and develop retired thoroughbred racehorses for their next chapter in life</h1>
    <span class="btn btn-ghost">Adopt a Thoroughbred</span>
    <span class="btn btn-green">Donate Us</span>
  </section>

  <section class="m-retire center">
    <h2 class="serif">Retire. Retrain.<br>Rehome.</h2>
    <p><strong>Corvale Paddock Rehoming Society</strong> (CPRS) is a registered not-for-profit organization in Alberta.</p>
    <div class="photo" role="img" aria-label="Black and white photo of a grey horse's head"></div>
  </section>

  <section class="m-about center">
    <h2 class="serif">What is<br>Thoroughbred<br>Aftercare?</h2>
    <p class="first"><strong>The health</strong>, <strong>safety</strong> and <strong>welfare</strong> of our equine athletes does not end at the finish line, and retirement and aftercare are critical to the success of the racing industry.</p>
    <p>Aftercare is the safe placement of racehorses after their careers as racehorse are completed. Some horses might retire to the breeding shed or broodmare bands, while others are retrained for second careers.</p>
    <span class="btn btn-green">Learn More About Us</span>
  </section>

  <div class="m-adopt-photo" role="img" aria-label="Sunlit photo of a woman with a dark bay horse"></div>

  <section class="m-adopt center">
    <h2 class="serif">Adopt a Horse</h2>
    <p>Corvale Paddock Rehoming is committed to helping match you with the perfect horse.</p>
    <span class="btn btn-green">Adopt Now</span>
  </section>

  <section class="m-horses center">
    <h2 class="serif">Our Horses</h2>
    <div class="cards">
      <article class="card">
        <div class="photo" role="img" aria-label="Photo of Marlowe Bay, a bay gelding"></div>
        <div class="name">Marlowe Bay</div>
        <span class="tag">Our Horses</span>
        <div class="fee">FEE $1,000—NOW $800<br>UNTIL 5/31</div>
        <div class="row">Height 15.3</div>
        <div class="row gap">Birth Year 2016</div>
        <div class="row" style="margin-top:3px">Color Bay<br>Gender Gelding</div>
        <div class="row gap">Location LEXINGTON, KY</div>
        <span class="read">Read More</span>
      </article>
      <article class="card">
        <div class="photo" role="img" aria-label="Photo of Tobin Reel, a chestnut gelding"></div>
        <div class="name">Tobin Reel</div>
        <span class="tag">Our Horses</span>
        <div class="fee">FEE $1,000—NOW $800<br>UNTIL 5/31</div>
        <div class="row">Height 15.3</div>
        <div class="row gap">Birth Year 2016</div>
        <div class="row" style="margin-top:3px">Color Bay<br>Gender Gelding</div>
        <div class="row gap">Location LEXINGTON, KY</div>
        <span class="read">Read More</span>
      </article>
      <article class="card">
        <div class="photo" role="img" aria-label="Photo of Quiet Harbor, a dark bay gelding"></div>
        <div class="name">Quiet Harbor</div>
        <span class="tag">Our Horses</span>
        <div class="fee">FEE $1,000—NOW $800<br>UNTIL 5/31</div>
        <div class="row">Height 15.3</div>
        <div class="row gap">Birth Year 2016</div>
        <div class="row" style="margin-top:3px">Color Bay<br>Gender Gelding</div>
        <div class="row gap">Location LEXINGTON, KY</div>
        <span class="read">Read More</span>
      </article>
    </div>
    <span class="btn btn-green">More Ways to Give</span>
  </section>

  <section class="m-contact">
    <h2 class="serif center">Have a question or need more information?</h2>
    <p class="lede center">Give us a call or use the form below.</p>
    <div class="info">
      <svg class="pin"><use href="#icon-pin"/></svg>
      <h3>Location</h3>
      42 Larkspur Run<br>Fenwick Hollow<br>British Columbia<br>V0X 2B7
    </div>
    <div class="info">
      <svg class="pin"><use href="#icon-pin"/></svg>
      <h3>Call Us</h3>
      +1 555 014 2290
    </div>
    <div class="info">
      <svg class="pin"><use href="#icon-pin"/></svg>
      <h3>E-Mail</h3>
      info@corvalepaddock.org
    </div>
    <form class="m-form">
      <div class="field"><label>Name <b>*</b></label><div class="input"></div></div>
      <div class="field"><label>Email <b>*</b></label><div class="input"></div></div>
      <div class="field"><label>Phone</label><div class="input"></div></div>
      <div class="field"><label>Message <b>*</b></label><div class="input"></div></div>
      <span class="btn btn-submit">Submit</span>
    </form>
  </section>

  <div class="m-gap"></div>

  <footer class="m-footer">
    <div class="foot-addr">
      <strong>Corvale Paddock Rehoming Society</strong>
      42 Larkspur Run<br>Fenwick Hollow<br>British Columbia<br>V0X 2B7<br>555-018-7734
    </div>
    <div class="foot-links">
      Home<br>About<br>Adopt<br>Horses<br><span class="pill">Donate &amp; Shop</span><br>Contact Us
    </div>
    <div class="social"><span class="round"></span><span class="round"></span><span></span></div>
    <p class="copy">Copyright © 2021. 0.0.0b. - Dev version</p>
  </footer>
</main>

</body>
</html>
```